Website for Plumbing Company, Sir FlowBoiler

I need a 7-page fully HTML-coded website for my plumbing company, Sir FlowBoiler. We specialize in installation, repair, and replacement of both gas and electric water heaters. Although we offer both tankless (on-demand) water heaters and standard (with tank) water heaters, most of our business is related to standard (with tank) water heaters in the USA market.

These are the pages I need:
1. Home page with sections such as About Us, Our Services, Why Choose Us, Testimonials, Location Map (Palm Beach County Florida), Quote Request Form, Join Our Newsletter, Mission Statement, etc.

2. Gas Water Heaters

3. Electric Water Heaters

4. Tankless Water Heaters

5. About Us

6. Contact Us

7. Privacy Policy, Terms & Conditions

Be sure to mention the following points:
1. Same-Day Service
2. Best Price Guarantee
3. 100% Satisfaction Rating
4. 15-Year Warranty on Water Heater & Parts
5. Lifetime Warranty on Workmanship
*All Warranties are Transferrable Upon Home Sale

Once design is selected and finalized, I need the website coded in a standard HTML/CSS and temporarily hosted on your development server so I can see the website functionality that is not observable from screenshots, such as section animations, etc. Once those details are finalized, I will move the source code to my server and complete the project.

Target Market(s)

Residential Home Owners and Business Owners

Industry/Entity Type

Plumbing, Home Services, Remodeling, Construction

Coding

Coded - Design and coding required

Number of Pages Required

5+ page

Colors
0054AA
0677BA
7BADD7
CADEEF
E8F1F8
FFC000
F8CF3A
FAE287
FDF2CF
FEFAEE
EE7325
F08F49
F5BC92
FAE3D3
FDF4ED

Requirements
Must have
• Clean, colorful, and professional

```html
<!DOCTYPE html>
<html lang="en">
<head>
<meta charset="utf-8">
<title>Sir FlowBoiler – Water Heater Solutions</title>
<link href="https://fonts.googleapis.com/css2?family=Montserrat:wght@700;800;900&family=Open+Sans:wght@400;600;700&display=swap" rel="stylesheet">
<style>
:root{
  --blue:#0054AA;--blue2:#0677BA;--blue3:#7BADD7;--blue4:#CADEEF;--blue5:#E8F1F8;
  --yellow:#FFC000;--yellow2:#F8CF3A;--yellow3:#FAE287;--yellow4:#FDF2CF;--yellow5:#FEFAEE;
  --orange:#EE7325;--orange2:#F08F49;--orange3:#F5BC92;--orange4:#FAE3D3;--orange5:#FDF4ED;
  --ink:#111827;--text:#374151;--muted:#6b7280;--navy:#111a2e;--paper:#f6f8fb;
}
*{box-sizing:border-box;margin:0;padding:0}
html,body{width:1200px;height:2524px;overflow:hidden}
body{font-family:"Open Sans",sans-serif;color:var(--text);background:#fff;position:relative}
h1,h2,h3,h4{font-family:"Montserrat",sans-serif;color:var(--ink)}
svg{display:block}
.wrap{width:570px;margin:0 auto;position:relative}
section,header,footer,.topbar{position:relative;width:1200px}

/* top bar */
.topbar{height:16px;background:var(--blue2);color:#fff;font-size:6.5px}
.topbar .wrap{display:flex;justify-content:space-between;align-items:center;height:16px}
.topbar .perks{display:flex;gap:12px}
.topbar span{display:flex;align-items:center;gap:4px}

/* nav */
.nav{height:53px;border-bottom:2px solid var(--orange2);background:#fff}
.nav .wrap{display:flex;align-items:center;height:51px}
.brand{display:flex;align-items:center;gap:5px;font-family:"Montserrat",sans-serif;font-weight:800;font-size:10px;color:var(--blue)}
.brand i{width:14px;height:14px;border-radius:50%;background:var(--blue);display:block}
.menu{display:flex;gap:4px;margin-left:88px;font-size:6.5px;font-weight:600;color:#333}
.menu a{padding:5px 6px;text-decoration:none;color:inherit}
.menu a.on{background:var(--orange);color:#fff}
.nav .cta{margin-left:auto;background:var(--yellow);color:var(--ink);font-weight:700;font-size:6.5px;padding:8px 15px;border-radius:14px;box-shadow:0 2px 4px rgba(0,0,0,.15)}

/* hero */
.hero{height:353px;background:linear-gradient(90deg,#0054AA 0%,#0864b4 55%,#2a6fb0 100%);overflow:hidden}
.hero .slant{position:absolute;top:0;right:0;width:300px;height:353px;background:linear-gradient(180deg,#3a79b4,#4c7fab);clip-path:polygon(96px 0,300px 0,300px 353px,28px 353px)}
.hero .wrap{height:353px}
.hero .tag{position:absolute;top:62px;left:0;background:var(--yellow);color:var(--ink);font-size:6px;font-weight:700;padding:4px 9px;letter-spacing:.1px}
.hero h1{position:absolute;top:90px;left:0;color:#fff;font-size:30px;line-height:35px;font-weight:900;width:280px;letter-spacing:-.3px}
.hero p{position:absolute;top:206px;left:0;width:275px;color:#e6efff;font-size:9.5px;line-height:15.5px}
.hero .btns{position:absolute;top:265px;left:0;display:flex;gap:8px}
.btn{display:inline-flex;align-items:center;justify-content:center;gap:5px;font-size:7px;font-weight:700;letter-spacing:.2px}
.hero .b1{background:var(--orange);color:#fff;width:113px;height:27px}
.hero .b2{background:#fff;color:var(--blue);width:102px;height:27px}
.hero .photo{position:absolute;top:88px;left:296px;width:274px;height:179px;border:4px solid #fff;background:linear-gradient(135deg,#b9c2cc 0%,#8b95a3 45%,#6a7483 100%);box-shadow:0 4px 12px rgba(0,0,0,.25)}

/* perks */
.perks-band{height:188px;background:var(--paper)}
.perk-row{display:flex;gap:11.3px;padding-top:31px}
.perk{width:134px;height:127px;background:#fff;border:2px solid var(--blue4);position:relative;text-align:center;padding-top:12px;overflow:hidden;box-shadow:0 2px 5px rgba(0,0,0,.05)}
.perk::after{content:"";position:absolute;top:0;right:0;border-top:30px solid var(--blue);border-left:30px solid transparent}
.perk .ic{width:37px;height:37px;border-radius:50%;background:var(--blue);margin:0 auto 8px;display:flex;align-items:center;justify-content:center}
.perk h3{font-size:14.5px;line-height:17px;font-weight:800;color:var(--ink)}
.perk p{font-size:6px;line-height:9px;color:#555;margin-top:6px;padding:0 10px}
.perk.hot{background:linear-gradient(135deg,var(--orange),var(--orange2));border-color:var(--yellow2)}
.perk.hot::after{border-top-color:var(--yellow)}
.perk.hot .ic{background:#fff}
.perk.hot h3,.perk.hot p{color:#fff}

/* section heads */
.pill{display:inline-block;font-size:6px;font-weight:700;padding:5px 12px;border-radius:2px}
.head{text-align:center}
.head h2{font-size:23px;font-weight:800;margin-top:8px;letter-spacing:-.2px}
.head p{font-size:9.5px;line-height:13.5px;color:#374151;margin:10px auto 0;width:360px}

/* services */
.services{height:413px;background:#fff;padding-top:38px}
.services .pill{background:var(--blue5);color:var(--blue)}
.svc-row{display:flex;gap:15px;margin-top:31px}
.svc{width:180px;height:219px;border:2px solid var(--blue3);background:#fff;position:relative}
.svc .top{height:58px;display:flex;align-items:center;gap:8px;padding:0 12px;position:relative;overflow:hidden}
.svc .top h3{color:#fff;font-size:14px;line-height:16px;font-weight:800;position:relative}
.svc .top .ic{width:29px;height:29px;border-radius:50%;display:flex;align-items:center;justify-content:center;flex:none;position:relative}
.svc .top::after{content:"";position:absolute;right:0;top:0;width:80px;height:58px;background:rgba(255,255,255,.15);clip-path:polygon(0 0,100% 0,100% 100%,70% 100%)}
.svc .body{padding:12px 12px 0}
.svc .body p{font-size:7.3px;line-height:12.5px;color:#444;margin-bottom:8px}
.svc ul{list-style:none}
.svc li{font-size:7.3px;line-height:18.3px;color:#333;display:flex;align-items:center;gap:6px}
.svc li::before{content:"";width:4px;height:4px;border-radius:50%;background:var(--dot)}
.svc .more{position:absolute;left:12px;bottom:12px;height:19px;width:79px;color:#fff;font-size:6px}
.svc.gas{border-color:var(--blue3);--dot:var(--yellow)}
.svc.gas .top{background:linear-gradient(90deg,var(--blue),var(--blue2))}
.svc.gas .ic{background:var(--yellow)}
.svc.gas .more{background:var(--blue)}
.svc.ele{border-color:var(--orange3);--dot:var(--blue)}
.svc.ele .top{background:linear-gradient(90deg,var(--orange),var(--orange2))}
.svc.ele .ic{background:var(--blue)}
.svc.ele .more{background:var(--orange)}
.svc.tkl{border-color:var(--yellow3);--dot:var(--blue)}
.svc.tkl .top{background:linear-gradient(90deg,var(--yellow),var(--yellow2))}
.svc.tkl .ic{background:var(--blue)}
.svc.tkl .more{background:var(--yellow)}

/* why */
.why{height:274px;background:linear-gradient(180deg,#0a60b4 0%,#0677BA 55%,#2b6fb3 100%);padding-top:36px}
.why .head h2{color:#fff}
.why .head p{color:#e2ecff;width:370px}
.why-row{display:flex;gap:15px;margin-top:32px}
.why-card{width:180px;height:105px;background:rgba(255,255,255,.13);border-left:3px solid var(--yellow);padding:16px 16px 0}
.why-card h3{color:#fff;font-size:11.5px;font-weight:800;margin-top:8px}
.why-card p{color:#d8e6f8;font-size:7px;line-height:12.5px;margin-top:7px}

/* reviews */
.reviews{height:376px;background:var(--paper);padding-top:42px}
.reviews .pill{background:var(--orange5);color:var(--orange)}
.rev-row{display:flex;gap:15px;margin-top:32px}
.rev{width:180px;height:133px;background:#fff;border-left:4px solid var(--orange);padding:12px 12px 0 12px;position:relative;box-shadow:0 2px 8px rgba(0,0,0,.06)}
.rev .stars{display:flex;gap:2px}
.rev .q{position:absolute;right:10px;top:9px}
.rev blockquote{font-size:7px;line-height:12.3px;color:#333;margin-top:6px;height:72px}
.rev .who{display:flex;justify-content:space-between;align-items:center;margin-top:4px}
.rev .who b{display:block;font-size:7.5px;color:var(--ink)}
.rev .who small{font-size:5.5px;color:#666}
.rev .chip{background:var(--blue5);color:var(--blue);font-size:5.5px;font-weight:700;padding:4px 7px}
.reviews .join{display:flex;margin:24px auto 0;width:140px;height:27px;background:var(--blue);color:#fff}

/* quote */
.quote{height:555px;background:#fff;padding-top:41px}
.quote .pill{background:var(--yellow5);color:var(--yellow);}
.quote .head h2{margin-top:10px}
.form{width:389px;margin:25px auto 0;border:2px solid var(--blue);background:#fff}
.form .fhead{height:57px;background:linear-gradient(90deg,var(--blue),var(--blue2));padding:12px 12px 0;position:relative;overflow:hidden}
.form .fhead::after{content:"";position:absolute;right:0;top:0;width:90px;height:57px;background:rgba(255,255,255,.12);clip-path:polygon(30% 0,100% 0,100% 100%,75% 100%)}
.form .fhead h3{color:#fff;font-size:15px;font-weight:800}
.form .fhead p{color:#dbe8fa;font-size:6.5px;margin-top:5px}
.fbody{padding:15px 15px 18px}
.grid{display:flex;gap:12px}
.field{flex:1;margin-bottom:13px}
.field label{display:block;font-size:6px;font-weight:700;color:var(--ink);margin-bottom:6px}
.box{height:25px;border:1px solid #cfd5dd;font-size:6.8px;color:#9aa3ad;padding:0 8px;display:flex;align-items:center;justify-content:space-between}
.box.sel{color:#333}
.box.area{height:63px;align-items:flex-start;padding-top:8px}
.submit{height:27px;background:linear-gradient(90deg,var(--orange),var(--orange2));color:#fff;display:flex;margin-top:2px}
.fine{text-align:center;font-size:5.5px;color:#555;margin-top:13px}

/* emergency */
.emergency{height:82px;background:linear-gradient(90deg,var(--orange),var(--orange2))}
.emergency .wrap{height:82px;display:flex;align-items:center;justify-content:space-between}
.emergency h3{color:#fff;font-size:14.5px;font-weight:800}
.emergency p{color:#fff;font-size:8.8px;margin-top:3px}
.emergency .call{background:#fff;color:var(--orange);width:126px;height:27px;box-shadow:0 2px 4px rgba(0,0,0,.12)}

/* footer */
.footer{height:183px;background:var(--navy);color:#cfd6e2}
.footer .wrap{display:flex;gap:22px;padding-top:22px}
.fcol{width:126px}
.fcol .brand{color:#fff;background:#fff;padding:6px;width:53px;height:29px;justify-content:center;font-size:0}
.fcol .brand i{width:12px;height:12px}
.fabout{font-size:6.8px;line-height:12px;margin-top:9px;color:#d6dce6}
.social{display:flex;gap:8px;margin-top:9px}
.social i{width:18px;height:18px;border-radius:50%;background:var(--blue2);display:block}
.fcol h4{color:#fff;font-size:10.5px;font-weight:800;padding-bottom:5px;border-bottom:1.5px solid var(--orange);margin-bottom:10px}
.fcol ul{list-style:none}
.fcol li{font-size:6.8px;line-height:18.3px;display:flex;align-items:center;gap:5px}
.fcol li::before{content:"";width:3px;height:3px;border-radius:50%;background:var(--orange)}
.contact div{display:flex;gap:7px;font-size:6.8px;line-height:10px;margin-bottom:10px}
.contact small{font-size:5.5px;color:#98a2b3}
.legal{height:31px;background:#0b1222;color:#9aa3b2;font-size:5.8px}
.legal .wrap{display:flex;justify-content:space-between;align-items:center;height:31px}
.legal nav{display:flex;gap:9px}
</style>
</head>
<body>

<div class="topbar">
  <div class="wrap">
    <div class="perks">
      <span><svg width="7" height="7" viewBox="0 0 24 24" fill="none" stroke="#fff" stroke-width="2.4"><circle cx="12" cy="12" r="9"/><path d="M12 7v5l3 2"/></svg>Same-Day Service</span>
      <span><svg width="7" height="7" viewBox="0 0 24 24" fill="none" stroke="#fff" stroke-width="2.4"><circle cx="12" cy="9" r="6"/><path d="M9 14l-2 8 5-3 5 3-2-8"/></svg>100% Satisfaction</span>
      <span><svg width="7" height="7" viewBox="0 0 24 24" fill="none" stroke="#fff" stroke-width="2.4"><path d="M12 3l8 3v6c0 5-4 8-8 9-4-1-8-4-8-9V6z"/></svg>Lifetime Warranty</span>
    </div>
    <span><svg width="7" height="7" viewBox="0 0 24 24" fill="none" stroke="#fff" stroke-width="2.4"><path d="M5 3h4l2 5-3 2a12 12 0 006 6l2-3 5 2v4a2 2 0 01-2 2A17 17 0 013 5a2 2 0 012-2z"/></svg>(561) 000-0142</span>
  </div>
</div>

<header class="nav">
  <div class="wrap">
    <div class="brand"><i></i>Sir FlowBoiler</div>
    <nav class="menu"><a class="on">HOME</a><a>GAS</a><a>ELECTRIC</a><a>TANKLESS</a><a>ABOUT</a><a>CONTACT</a></nav>
    <a class="cta">GET FREE QUOTE</a>
  </div>
</header>

<section class="hero">
  <div class="slant"></div>
  <div class="wrap">
    <div class="tag">PALM BEACH COUNTY'S #1 WATER HEATER EXPERTS</div>
    <h1>Fast, Reliable Water Heater Solutions</h1>
    <p>Same-day installation, repair &amp; replacement. Lifetime warranty on workmanship. 100% satisfaction guaranteed or your money back.</p>
    <div class="btns"><a class="btn b1">GET FREE QUOTE NOW</a><a class="btn b2">CALL (561) 000-0142</a></div>
    <div class="photo" role="img" aria-label="Technician standing beside tank and tankless water heaters in a warehouse"></div>
  </div>
</section>

<section class="perks-band">
  <div class="wrap perk-row">
    <div class="perk"><div class="ic"><svg width="18" height="18" viewBox="0 0 24 24" fill="none" stroke="#fff" stroke-width="2.2"><circle cx="12" cy="12" r="9"/><path d="M12 7v5l3 2"/></svg></div><h3>Same-Day<br>Service</h3><p>Fast response times - we'll be there when you need us most</p></div>
    <div class="perk hot"><div class="ic"><svg width="18" height="18" viewBox="0 0 24 24" fill="none" stroke="#EE7325" stroke-width="2.4"><path d="M12 2v20M17 6H9.5a3.5 3.5 0 000 7h5a3.5 3.5 0 010 7H6"/></svg></div><h3>Best Price<br>Guarantee</h3><p>We'll beat any competitor's written estimate</p></div>
    <div class="perk"><div class="ic"><svg width="18" height="18" viewBox="0 0 24 24" fill="none" stroke="#fff" stroke-width="2.2"><path d="M7 10v11H3V10zM7 10l4-8a3 3 0 013 3v4h6a2 2 0 012 2l-2 8a2 2 0 01-2 2H7"/></svg></div><h3>100%<br>Satisfaction</h3><p>Perfect rating from over 500+ happy customers</p></div>
    <div class="perk"><div class="ic"><svg width="18" height="18" viewBox="0 0 24 24" fill="none" stroke="#fff" stroke-width="2.2"><path d="M12 3l8 3v6c0 5-4 8-8 9-4-1-8-4-8-9V6z"/></svg></div><h3>Lifetime<br>Warranty</h3><p>15-year parts + lifetime workmanship guarantee</p></div>
  </div>
</section>

<section class="services">
  <div class="wrap">
    <div class="head">
      <span class="pill">OUR SERVICES</span>
      <h2>Water Heater Solutions for Every Need</h2>
      <p>From traditional tank systems to modern tankless units, we install, repair, and maintain all types of water heaters.</p>
    </div>
    <div class="svc-row">
      <div class="svc gas">
        <div class="top"><div class="ic"><svg width="14" height="14" viewBox="0 0 24 24" fill="none" stroke="#fff" stroke-width="2.2"><path d="M12 2c1 4 6 6 6 12a6 6 0 01-12 0c0-3 2-5 3-6 0 3 2 4 3 4 0-4-1-7 0-10z"/></svg></div><h3>Gas Water<br>Heaters</h3></div>
        <div class="body">
          <p>Energy-efficient gas-powered systems for reliable hot water supply.</p>
          <ul><li>Harbor Crest &amp; Thermoline models</li><li>Energy-efficient operation</li><li>Professional installation</li><li>Same-day service available</li></ul>
        </div>
        <a class="btn more">LEARN MORE <svg width="8" height="8" viewBox="0 0 24 24" fill="none" stroke="#fff" stroke-width="2.6"><path d="M5 12h14M13 6l6 6-6 6"/></svg></a>
      </div>
      <div class="svc ele">
        <div class="top"><div class="ic"><svg width="14" height="14" viewBox="0 0 24 24" fill="none" stroke="#fff" stroke-width="2.2"><path d="M13 2L4 14h7l-1 8 9-12h-7z"/></svg></div><h3>Electric Water<br>Heaters</h3></div>
        <div class="body">
          <p>Safe, efficient electric units perfect for any home or business.</p>
          <ul><li>Ridgeway &amp; Coastal Heat models</li><li>Lower installation costs</li><li>Safe &amp; reliable</li><li>Expert repairs &amp; maintenance</li></ul>
        </div>
        <a class="btn more">LEARN MORE <svg width="8" height="8" viewBox="0 0 24 24" fill="none" stroke="#fff" stroke-width="2.6"><path d="M5 12h14M13 6l6 6-6 6"/></svg></a>
      </div>
      <div class="svc tkl">
        <div class="top"><div class="ic"><svg width="14" height="14" viewBox="0 0 24 24" fill="none" stroke="#fff" stroke-width="2.2"><path d="M12 3s6 7 6 11a6 6 0 01-12 0c0-4 6-11 6-11z"/></svg></div><h3>Tankless<br>Water Heaters</h3></div>
        <div class="body">
          <p>On-demand hot water with superior energy efficiency and space savings.</p>
          <ul><li>Endless hot water supply</li><li>Up to 30% energy savings</li><li>Space-saving design</li><li>Longer lifespan (20+ years)</li></ul>
        </div>
        <a class="btn more">LEARN MORE <svg width="8" height="8" viewBox="0 0 24 24" fill="none" stroke="#fff" stroke-width="2.6"><path d="M5 12h14M13 6l6 6-6 6"/></svg></a>
      </div>
    </div>
  </div>
</section>

<section class="why">
  <div class="wrap">
    <div class="head">
      <h2>Why Palm Beach Trusts Us</h2>
      <p>Over 20 years of experience serving Palm Beach County with honest, professional water heater services.</p>
    </div>
    <div class="why-row">
      <div class="why-card"><svg width="20" height="16" viewBox="0 0 24 18" fill="none" stroke="#FFC000" stroke-width="2"><path d="M2 15l7-7 4 4 8-8M15 4h6v6"/></svg><h3>Licensed &amp; Insured</h3><p>Fully licensed, bonded, and insured for your peace of mind and protection.</p></div>
      <div class="why-card"><svg width="20" height="20" viewBox="0 0 24 24" fill="none" stroke="#FFC000" stroke-width="2"><path d="M14.7 6.3a4 4 0 005 5L21 13l-2 2-1.3-1.3a4 4 0 01-5-5L4 17.4 6.6 20l8.7-8.7"/></svg><h3>Expert Technicians</h3><p>Certified professionals with extensive training on all major brands and models.</p></div>
      <div class="why-card"><svg width="22" height="20" viewBox="0 0 26 24" fill="none" stroke="#FFC000" stroke-width="2"><circle cx="9" cy="7" r="4"/><path d="M2 21v-2a5 5 0 015-5h4a5 5 0 015 5v2M17 3a4 4 0 010 8M24 21v-2a5 5 0 00-4-5"/></svg><h3>Local Family Business</h3><p>Proudly serving our Palm Beach neighbors with personalized, honest service.</p></div>
    </div>
  </div>
</section>

<section class="reviews">
  <div class="wrap">
    <div class="head">
      <span class="pill">CUSTOMER REVIEWS</span>
      <h2>What Our Customers Say</h2>
      <p>Don't just take our word for it - hear from our satisfied customers across Palm Beach County.</p>
    </div>
    <div class="rev-row">
      <div class="rev">
        <div class="stars"><svg width="48" height="8" viewBox="0 0 60 10"><g fill="#FFC000"><path id="st" d="M5 0l1.5 3.2 3.5.4-2.6 2.4.7 3.5L5 7.8 1.9 9.5l.7-3.5L0 3.6l3.5-.4z"/><use href="#st" x="12"/><use href="#st" x="24"/><use href="#st" x="36"/><use href="#st" x="48"/></g></svg></div>
        <svg class="q" width="26" height="20" viewBox="0 0 26 20" fill="#E8F1F8"><rect x="0" y="0" width="11" height="12" rx="2"/><path d="M6 12h5l-3 8H4z"/><rect x="14" y="0" width="11" height="12" rx="2"/><path d="M20 12h5l-3 8h-4z"/></svg>
        <blockquote>"Absolutely fantastic service! They installed our new tankless water heater in just 4 hours. The technician was professional, clean, and explained everything clearly. Highly recommend!"</blockquote>
        <div class="who"><div><b>Dana Whitfield</b><small>West Palm Beach, FL</small></div><span class="chip">TANKLESS INSTALL</span></div>
      </div>
      <div class="rev">
        <div class="stars"><svg width="48" height="8" viewBox="0 0 60 10"><g fill="#FFC000"><use href="#st"/><use href="#st" x="12"/><use href="#st" x="24"/><use href="#st" x="36"/><use href="#st" x="48"/></g></svg></div>
        <svg class="q" width="26" height="20" viewBox="0 0 26 20" fill="#E8F1F8"><rect x="0" y="0" width="11" height="12" rx="2"/><path d="M6 12h5l-3 8H4z"/><rect x="14" y="0" width="11" height="12" rx="2"/><path d="M20 12h5l-3 8h-4z"/></svg>
        <blockquote>"Our water heater failed on a Sunday morning. They came out within 2 hours and had it fixed quickly. Fair pricing and excellent work. These guys are the real deal!"</blockquote>
        <div class="who"><div><b>Marco Valente</b><small>Boca Raton, FL</small></div><span class="chip">EMERGENCY REPAIR</span></div>
      </div>
      <div class="rev">
        <div class="stars"><svg width="48" height="8" viewBox="0 0 60 10"><g fill="#FFC000"><use href="#st"/><use href="#st" x="12"/><use href="#st" x="24"/><use href="#st" x="36"/><use href="#st" x="48"/></g></svg></div>
        <svg class="q" width="26" height="20" viewBox="0 0 26 20" fill="#E8F1F8"><rect x="0" y="0" width="11" height="12" rx="2"/><path d="M6 12h5l-3 8H4z"/><rect x="14" y="0" width="11" height="12" rx="2"/><path d="M20 12h5l-3 8h-4z"/></svg>
        <blockquote>"Best experience I've had with any contractor. They were on time, professional, and the price was exactly what they quoted. The new water heater works perfectly. Thank you!"</blockquote>
        <div class="who"><div><b>Priya Holloway</b><small>Delray Beach, FL</small></div><span class="chip">GAS REPLACEMENT</span></div>
      </div>
    </div>
    <a class="btn join">JOIN OUR HAPPY CUSTOMERS</a>
  </div>
</section>

<section class="quote">
  <div class="wrap">
    <div class="head">
      <span class="pill">FREE QUOTE</span>
      <h2>Ready to Get Started?</h2>
      <p>Request a free, no-obligation quote today. We'll respond within 24 hours!</p>
    </div>
  </div>
  <div class="form">
    <div class="fhead"><h3>Get Your Free Quote</h3><p>Fill out the form below and we'll get back to you within 24 hours</p></div>
    <div class="fbody">
      <div class="grid">
        <div class="field"><label>FULL NAME *</label><div class="box">John Smith</div></div>
        <div class="field"><label>PHONE NUMBER *</label><div class="box">(561) 000-0000</div></div>
      </div>
      <div class="grid">
        <div class="field"><label>EMAIL ADDRESS *</label><div class="box">john@example.com</div></div>
        <div class="field"><label>SERVICE NEEDED *</label><div class="box sel">Select a service <svg width="6" height="6" viewBox="0 0 10 10" fill="none" stroke="#333" stroke-width="1.5"><path d="M2 4l3 3 3-3"/></svg></div></div>
      </div>
      <div class="field"><label>SERVICE ADDRESS *</label><div class="box">123 Main St, Palm Beach, FL</div></div>
      <div class="field"><label>ADDITIONAL DETAILS</label><div class="box area">Tell us about your water heater needs...</div></div>
      <a class="btn submit">REQUEST FREE QUOTE <svg width="9" height="9" viewBox="0 0 24 24" fill="none" stroke="#fff" stroke-width="2.2"><path d="M22 2L11 13M22 2l-7 20-4-9-9-4z"/></svg></a>
      <p class="fine">By submitting this form, you agree to be contacted by SIR FLOWBOILER regarding your request.</p>
    </div>
  </div>
</section>

<section class="emergency">
  <div class="wrap">
    <div><h3>Water Heater Emergency?</h3><p>We offer 24/7 emergency service throughout Palm Beach County</p></div>
    <a class="btn call">CALL NOW: (561) 000-0142</a>
  </div>
</section>

<footer class="footer">
  <div class="wrap">
    <div class="fcol">
      <div class="brand"><i></i></div>
      <p class="fabout">Palm Beach County's trusted water heater experts. Same-day service, lifetime warranty, 100% satisfaction guaranteed.</p>
      <div class="social"><i></i><i></i><i></i></div>
    </div>
    <div class="fcol"><h4>OUR SERVICES</h4><ul><li>Gas Water Heaters</li><li>Electric Water Heaters</li><li>Tankless Water Heaters</li><li>Emergency Repairs</li><li>Maintenance Plans</li></ul></div>
    <div class="fcol"><h4>QUICK LINKS</h4><ul><li>Home</li><li>About Us</li><li>Contact</li><li>Privacy Policy</li><li>Terms of Service</li></ul></div>
    <div class="fcol contact"><h4>CONTACT US</h4>
      <div><svg width="8" height="8" viewBox="0 0 24 24" fill="none" stroke="#EE7325" stroke-width="2.4"><path d="M5 3h4l2 5-3 2a12 12 0 006 6l2-3 5 2v4a2 2 0 01-2 2A17 17 0 013 5a2 2 0 012-2z"/></svg><span>(561) 000-0142<br><small>24/7 Emergency</small></span></div>
      <div><svg width="8" height="8" viewBox="0 0 24 24" fill="none" stroke="#EE7325" stroke-width="2.4"><rect x="2" y="5" width="20" height="14" rx="2"/><path d="M2 7l10 6 10-6"/></svg><span>info@sirflowboiler.com</span></div>
      <div><svg width="8" height="8" viewBox="0 0 24 24" fill="none" stroke="#EE7325" stroke-width="2.4"><path d="M12 22s7-7 7-12a7 7 0 00-14 0c0 5 7 12 7 12z"/><circle cx="12" cy="10" r="2.5"/></svg><span>Palm Beach County, FL<br>Serving all areas</span></div>
      <div><svg width="8" height="8" viewBox="0 0 24 24" fill="none" stroke="#EE7325" stroke-width="2.4"><circle cx="12" cy="12" r="9"/><path d="M12 7v5l3 2"/></svg><span>Mon-Fri: 7AM - 7PM<br>Sat-Sun: 8AM - 5PM</span></div>
    </div>
  </div>
</footer>
<div class="legal">
  <div class="wrap">
    <span>© 2026 SIR FLOWBOILER. All rights reserved.</span>
    <nav><span>Licensed &amp; Insured</span><span>•</span><span>Bonded Professionals</span><span>•</span><span>Lifetime Warranty</span></nav>
  </div>
</div>
</body>
</html>
```